Vantor Business card and stationary
I need double sided standard sized Business Card [3.5" x 2"]
Leave the font with designers creativity
Professional
Dean Holbrek
Director
P.O Box 481, Ferndale Ridge, NSW 1742
dean@vantorbuildco.com.au
www.vantorbuildco.com.au
Builders Lic No: 371506K
ABN: 83207594116
ACN: 207594116
Also please include united Trades Guild Logo in front side of business card.
One Call Gets It All.
Complete Building Solutions,
Project Management, New Constructions. Extensions, Renovations, Alterations, Remoulding, Kitchen renovations, Bathroom Renovations, Strata works, Building Maintenance, Insurance works, Fully Licensed & Insured, Member Of RTF, Member Of united Trades Guilds

```html
<!DOCTYPE html>
<html lang="en">
<head>
<meta charset="utf-8">
<title>Vantor Stationery Set</title>
<link href="https://fonts.googleapis.com/css2?family=Montserrat:wght@600;800&family=Open+Sans:wght@400;600&display=swap" rel="stylesheet">
<style>
:root{
  --bg:#2e2e30;
  --paper:#ffffff;
  --red:#d3141c;
  --red-dark:#9c0d12;
  --ink:#3a3a3a;
  --grey:#8a8a8c;
  --grey-light:#c9c9cb;
  --black:#111111;
  --label:#9a9a9a;
}
*{box-sizing:border-box;margin:0;padding:0}
html,body{width:1200px;height:408px;overflow:hidden;background:var(--bg);font-family:"Open Sans",sans-serif}
.board{position:relative;width:1200px;height:408px}
.item{position:absolute;box-shadow:0 3px 8px rgba(0,0,0,.45)}
.label{position:absolute;font-size:5px;color:var(--label);text-align:center;letter-spacing:.2px}
.brand{font-family:"Montserrat",sans-serif;font-weight:800;color:var(--red);letter-spacing:1px;display:flex;align-items:center;gap:3px;line-height:1}
.brand i{display:block;width:.7em;height:.7em;background:currentColor}
.brand.white{color:var(--paper)}
/* business cards */
.card{width:137px;height:79px;background:var(--paper);overflow:hidden}
.card .bar{position:absolute;left:0;right:0;bottom:0;height:5px;background:linear-gradient(90deg,var(--red-dark),var(--red))}
.card-front .person{position:absolute;left:9px;top:10px;font-family:"Montserrat",sans-serif;font-weight:600;font-size:6px;color:var(--red)}
.card-front .role{position:absolute;left:9px;top:18px;font-size:4px;color:var(--ink)}
.card-front .contacts{position:absolute;left:9px;top:28px;font-size:3.4px;line-height:5.2px;color:var(--ink)}
.card-front .brand{position:absolute;right:8px;top:10px;font-size:8px}
.card-front .guild{position:absolute;right:10px;bottom:12px;width:16px;height:16px;border-radius:50%;background:var(--grey-light)}
.card-back .services{position:absolute;left:8px;top:8px;font-size:3.4px;line-height:5.2px;color:var(--ink);list-style:none}
.card-back .services li::before{content:"";display:inline-block;width:2.4px;height:2.4px;background:var(--red);margin-right:2px;vertical-align:middle}
.card-back .brand{position:absolute;right:8px;top:22px;font-size:9px}
.card-back .tag{position:absolute;right:8px;top:36px;font-size:3.6px;color:var(--ink)}
.card-dark{background:var(--black)}
.card-dark .brand{position:absolute;left:0;right:0;top:24px;justify-content:center;font-size:11px}
.card-dark .tag{position:absolute;left:0;right:0;top:40px;text-align:center;font-size:4px;color:var(--paper)}
.card-dark .line{position:absolute;left:0;right:0;top:52px;text-align:center;font-size:3.2px;color:var(--grey-light)}
/* letterheads */
.letterhead{width:221px;height:324px;background:var(--paper);overflow:hidden}
.letterhead .band{position:absolute;left:0;right:0;top:0;height:30px;background:linear-gradient(180deg,var(--red),var(--red-dark))}
.letterhead .crest{position:absolute;left:70px;top:6px;width:81px;height:34px;background:var(--paper);display:flex;align-items:center;justify-content:center}
.letterhead .crest .brand{font-size:11px}
.letterhead .head-info{position:absolute;right:8px;top:5px;font-size:3.2px;line-height:4.6px;color:var(--paper);text-align:right}
.letterhead .faint{position:absolute;left:20px;right:20px;bottom:16px;height:50px;background:linear-gradient(180deg,rgba(211,20,28,0),rgba(211,20,28,.1))}
.letterhead .foot{position:absolute;left:0;right:0;bottom:7px;text-align:center;font-size:3.2px;color:var(--ink)}
.letterhead .foot-rule{position:absolute;left:0;right:0;bottom:3px;height:2px;background:var(--red)}
/* envelopes */
.envelope{width:295px;height:103px;overflow:hidden}
.envelope svg{position:absolute;left:0;top:0}
.env-grey{background:var(--grey)}
.env-red{background:linear-gradient(180deg,var(--red),var(--red-dark))}
.env-white{background:var(--paper)}
.envelope .brand{position:absolute;left:0;right:0;top:30px;justify-content:center;font-size:12px}
.env-front{width:206px;height:108px;background:var(--paper);overflow:hidden}
.env-front .band{position:absolute;left:0;right:0;top:0;height:26px;background:linear-gradient(180deg,var(--red),var(--red-dark))}
.env-front .brand{position:absolute;left:12px;top:34px;font-size:10px}
.env-front .addr{position:absolute;left:12px;top:48px;font-size:3.2px;color:var(--ink)}
.env-front .faint{position:absolute;left:60px;right:20px;bottom:8px;height:38px;background:linear-gradient(180deg,rgba(211,20,28,0),rgba(211,20,28,.09))}
</style>
</head>
<body>
<main class="board">

  <!-- business cards -->
  <section class="item card card-front" style="left:91px;top:151px">
    <p class="person">Dean Holbrek</p>
    <p class="role">Director</p>
    <p class="contacts">P.O Box 481, Ferndale Ridge, NSW 1742<br>dean@vantorbuildco.com.au<br>www.vantorbuildco.com.au<br>Builders Lic No: 371506K<br>ABN: 83207594116 &nbsp;ACN: 207594116</p>
    <div class="brand"><i></i>VANTOR</div>
    <div class="guild" role="img" aria-label="united Trades Guild badge"></div>
    <div class="bar"></div>
  </section>
  <p class="label" style="left:91px;top:232px;width:137px">Business Card Front</p>

  <section class="item card card-back" style="left:91px;top:240px">
    <ul class="services">
      <li>Project Management</li><li>New Constructions</li><li>Extensions &amp; Renovations</li>
      <li>Kitchen &amp; Bathroom</li><li>Strata works</li><li>Building Maintenance</li>
      <li>Insurance works</li><li>Fully Licensed &amp; Insured</li>
    </ul>
    <div class="brand"><i></i>VANTOR</div>
    <p class="tag">One Call Gets It All.</p>
    <div class="bar"></div>
  </section>
  <p class="label" style="left:91px;top:322px;width:137px">Business Card Back</p>

  <section class="item card card-dark" style="left:91px;top:330px;height:62px">
    <div class="brand"><i></i>VANTOR</div>
    <p class="tag">Complete Building Solutions</p>
    <p class="line">Member Of RTF · Member Of united Trades Guilds</p>
  </section>
  <p class="label" style="left:91px;top:396px;width:137px">Business Card Dark</p>

  <!-- letterheads -->
  <section class="item letterhead" style="left:288px;top:36px">
    <div class="band"></div>
    <p class="head-info">dean@vantorbuildco.com.au<br>www.vantorbuildco.com.au<br>P.O Box 481, Ferndale Ridge</p>
    <div class="crest"><div class="brand"><i></i>VANTOR</div></div>
    <div class="faint" role="img" aria-label="faint house roofline decoration"></div>
    <p class="foot">P.O Box 481, Ferndale Ridge, NSW 1742 · ABN 83207594116 · Lic 371506K</p>
    <div class="foot-rule"></div>
  </section>
  <p class="label" style="left:288px;top:364px;width:221px">Letterhead Page 1</p>

  <section class="item letterhead" style="left:552px;top:36px">
    <div class="faint" role="img" aria-label="faint house roofline decoration"></div>
    <p class="foot">P.O Box 481, Ferndale Ridge, NSW 1742 · ABN 83207594116 · Lic 371506K</p>
    <div class="foot-rule"></div>
  </section>
  <p class="label" style="left:552px;top:364px;width:221px">Letterhead Page 2</p>

  <!-- envelopes -->
  <section class="item envelope env-grey" style="left:833px;top:36px">
    <svg width="295" height="103" viewBox="0 0 295 103"><path d="M0 0 L147.5 52 L295 0" fill="none" stroke="#a3a3a5" stroke-width="1"/></svg>
    <div class="brand white"><i></i>VANTOR</div>
  </section>

  <section class="item envelope env-red" style="left:833px;top:91px">
    <svg width="295" height="103" viewBox="0 0 295 103"><path d="M0 0 L147.5 50 L295 0" fill="none" stroke="#e8464c" stroke-width="1"/></svg>
    <div class="brand white"><i></i>VANTOR</div>
  </section>

  <section class="item envelope env-white" style="left:833px;top:168px;height:96px">
    <svg width="295" height="96" viewBox="0 0 295 96"><path d="M0 0 L147.5 30 L295 0 Z" fill="#d3141c"/></svg>
  </section>

  <section class="item env-front" style="left:833px;top:240px">
    <div class="band"></div>
    <div class="brand"><i></i>VANTOR</div>
    <p class="addr">P.O Box 481, Ferndale Ridge, NSW 1742</p>
    <div class="faint" role="img" aria-label="faint house roofline decoration"></div>
  </section>
  <p class="label" style="left:833px;top:358px;width:295px">Envelope Set DL</p>

</main>
</body>
</html>
```